New business card for civil engineering company - "Keel Survey"

We need a business card designed for our new structural engineering company.

The company name is "Keel Survey" logo files attached.

We would like the following:
* Two-sided card
* Simple design

Information to be placed on the card:
Name - Marcus Hollby
Job Title - Director / Structural Engineer
Credentials - BEng(Hons), CPEng, CMengNZ, IntPE(NZ)
Email - marcus.hollby@keelsurvey-example.co.nz
mobile - 0219036458
website - www.keelsurvey-example.co.nz

```html
<!DOCTYPE html>
<html lang="en">
<head>
<meta charset="utf-8">
<title>Keel Survey — Business Card</title>
<link rel="stylesheet" href="https://fonts.googleapis.com/css2?family=Lato:ital,wght@0,400;0,700;0,900;1,400&family=Exo+2:wght@700&display=swap">
<style>
  :root {
    --backdrop: #d9d9d9;
    --card-white: #ffffff;
    --brand-blue: #1f7fd0;
    --blue-light: #25a9e3;
    --blue-deep: #1b7fcf;
    --ink: #2f2f2f;
    --ink-soft: #3a3a3a;
    --muted: #8a8a8a;
    --rule: #d6d6d6;
  }
  * { margin: 0; padding: 0; box-sizing: border-box; }
  html, body { width: 1200px; height: 802px; overflow: hidden; }
  body {
    background: var(--backdrop);
    font-family: "Lato", sans-serif;
    position: relative;
  }
  .card {
    position: absolute;
    top: 274px;
    width: 443px;
    height: 265px;
    box-shadow: 0 3px 6px rgba(0,0,0,0.35);
  }
  .card--front { left: 136px; background: var(--card-white); }
  .card--back {
    left: 624px;
    background: linear-gradient(135deg, var(--blue-light) 0%, #22a0df 50%, var(--blue-deep) 100%);
    color: #fff;
    text-align: center;
  }

  /* front: brand lockup */
  .brand {
    position: absolute;
    left: 30px;
    top: 176px;
    width: 135px;
    text-align: center;
  }
  .brand__name {
    font-weight: 700;
    font-size: 15px;
    letter-spacing: 1.5px;
    color: var(--ink);
    text-transform: uppercase;
    white-space: nowrap;
  }
  .brand__tagline {
    margin-top: 3px;
    font-size: 6.5px;
    letter-spacing: 1.6px;
    color: var(--muted);
    text-transform: uppercase;
    white-space: nowrap;
  }
  .divider {
    position: absolute;
    left: 175px;
    top: 59px;
    width: 1px;
    height: 154px;
    background: var(--rule);
  }

  /* front: person details */
  .person {
    position: absolute;
    left: 192px;
    top: 72px;
  }
  .person__name {
    font-family: "Exo 2", sans-serif;
    font-weight: 700;
    font-size: 16.5px;
    color: var(--brand-blue);
    text-transform: uppercase;
    line-height: 1.1;
  }
  .person__title, .person__creds {
    font-size: 12.5px;
    color: var(--ink-soft);
    line-height: 17px;
  }
  .person__creds { font-style: italic; }

  .contact {
    position: absolute;
    left: 192px;
    top: 148px;
    list-style: none;
  }
  .contact__item {
    display: flex;
    align-items: center;
    gap: 4px;
    font-size: 12.5px;
    color: var(--ink-soft);
    line-height: 16.5px;
    white-space: nowrap;
  }
  .contact__icon { width: 9px; height: 10px; flex: none; }

  /* back */
  .back__name {
    position: absolute;
    left: 0; right: 0;
    top: 104px;
    font-weight: 400;
    font-size: 30px;
    letter-spacing: 4px;
    text-transform: uppercase;
    line-height: 1;
  }
  .back__tagline {
    position: absolute;
    left: 0; right: 0;
    top: 143px;
    font-size: 12.5px;
    letter-spacing: 3.5px;
    text-transform: uppercase;
  }
</style>
</head>
<body>
  <section class="card card--front" aria-label="Business card front">
    <div class="brand">
      <div class="brand__name">Keel Survey</div>
      <div class="brand__tagline">Peer Review Specialists</div>
    </div>
    <div class="divider"></div>
    <div class="person">
      <div class="person__name">Marcus Hollby</div>
      <div class="person__title">Director / Structural Engineer</div>
      <div class="person__creds">BEng(Hons), CPEng, CMengNZ, IntPE(NZ)</div>
    </div>
    <ul class="contact">
      <li class="contact__item">
        <svg class="contact__icon" viewBox="0 0 9 10" aria-hidden="true"><rect x="1.5" y="0.5" width="6" height="9" rx="1.2" fill="none" stroke="#1f7fd0" stroke-width="1.2"/><rect x="3.5" y="7.5" width="2" height="1" fill="#1f7fd0"/></svg>
        0219036458
      </li>
      <li class="contact__item">
        <svg class="contact__icon" viewBox="0 0 9 10" aria-hidden="true"><rect x="0.5" y="2" width="8" height="6" fill="#1f7fd0"/><path d="M0.8 2.4 L4.5 5.4 L8.2 2.4" fill="none" stroke="#fff" stroke-width="0.9"/></svg>
        marcus.hollby@keelsurvey-example.co.nz
      </li>
      <li class="contact__item">
        <svg class="contact__icon" viewBox="0 0 9 10" aria-hidden="true"><circle cx="4.5" cy="5" r="4" fill="#1f7fd0"/><path d="M2.5 3.5 Q4 3 4.5 4.5 Q5 6 6.5 6.5" fill="none" stroke="#fff" stroke-width="0.9"/></svg>
        www.keelsurvey-example.co.nz
      </li>
    </ul>
  </section>

  <section class="card card--back" aria-label="Business card back">
    <div class="back__name">Keel Survey</div>
    <div class="back__tagline">Peer Review Specialists</div>
  </section>
</body>
</html>
```